Retractable Banner Design for Gentle Paws Carolina Rebrand

We need a retractable banner design for our market booth. I absolutely love our old banner design and would like to keep it clean and similar but more on theme with the new brand with the new colors. Full brand guide attached. Our slogan we would like to include is "professional pet care for when you can't be there" (dog walking & pet sitting).
Our services we would like to include is: Extended Visits, Pop In Visits, Dog Walking, Pet Taxi, Travel & Adventure Hikes.
We offer: Discounts for First Responders, Teachers, & Military
I would like to use elements from the brand as well as the colors. Include the website www.gentlepawsco.net somewhere

```html
<!DOCTYPE html>
<html lang="en">
<head>
<meta charset="utf-8">
<title>Gentle Paws Carolina – Retractable Banner</title>
<link rel="stylesheet" href="https://fonts.googleapis.com/css2?family=Fira+Sans+Extra+Condensed:wght@600;700&family=Open+Sans:ital,wght@0,700;1,700&display=swap">
<style>
  :root {
    --backdrop: #18181a;
    --paper: #ffffff;
    --navy: #2b5873;
    --band-blue: #3c7190;
    --sun: #ecd47b;
    --berry: #b8357f;
    --white: #ffffff;
    --photo-light: #eef3f6;
    --photo-warm: #d9b888;
  }
  * { margin: 0; padding: 0; box-sizing: border-box; }
  html, body { width: 991px; height: 1200px; overflow: hidden; background: var(--backdrop); }
  .canvas { position: relative; width: 991px; height: 1200px; }
  .banner {
    position: absolute; left: 317px; top: 180px; width: 357px; height: 840px;
    background: var(--paper); overflow: hidden;
    font-family: "Fira Sans Extra Condensed", sans-serif;
  }
  .brand-name {
    position: absolute; top: 40px; left: 0; width: 100%;
    text-align: center; color: var(--navy);
    font-weight: 700; font-size: 38px; line-height: 1;
  }
  .brand-name span { display: block; }
  .hero-photo {
    position: absolute; left: 0; top: 128px; width: 357px; height: 300px;
    background: radial-gradient(ellipse at 55% 60%, var(--photo-warm) 0%, #e8d6bd 40%, var(--photo-light) 75%, var(--paper) 100%);
  }
  .blue-band { position: absolute; left: 0; top: 0; width: 357px; height: 840px; }
  .headline {
    position: absolute; top: 451px; left: 0; width: 100%;
    text-align: center; color: var(--sun);
    font-weight: 700; font-size: 31px; line-height: 31px; letter-spacing: 0.2px;
  }
  .tagline {
    position: absolute; top: 549px; left: 100px; width: 160px;
    text-align: center; color: var(--white);
    font-family: "Open Sans", sans-serif; font-style: italic; font-weight: 700;
    font-size: 17px; line-height: 21px;
  }
  .team-photo {
    position: absolute; width: 108px; height: 108px; border-radius: 50%;
    border: 3px solid var(--white);
    box-shadow: 0 3px 6px rgba(0,0,0,0.25);
  }
  .team-photo.left { left: -4px; top: 531px; background: radial-gradient(circle at 55% 60%, #3b2c24 0%, #5d6a4a 55%, #aebfc6 100%); }
  .team-photo.right { left: 251px; top: 548px; background: radial-gradient(circle at 45% 65%, #d9894a 0%, #4a3a33 45%, #c9a98c 100%); }
  .section-pill {
    position: absolute; left: 107px; width: 144px; height: 26px;
    background: var(--berry); border-radius: 5px;
    color: var(--white); text-align: center;
    font-weight: 600; font-size: 21px; line-height: 26px;
  }
  .section-pill.services { top: 643px; }
  .section-pill.offer { top: 727px; }
  .section-text {
    position: absolute; left: 0; width: 100%;
    text-align: center; color: var(--berry);
    font-weight: 600; font-size: 17.5px; line-height: 20.5px;
  }
  .section-text.services { top: 674px; }
  .section-text.offer { top: 759px; }
  .footer-bar {
    position: absolute; left: 0; bottom: 0; width: 100%; height: 32px;
    background: var(--berry); color: var(--white); text-align: center;
    font-family: "Open Sans", sans-serif; font-weight: 700; font-size: 13.5px; line-height: 32px;
  }
</style>
</head>
<body>
<div class="canvas">
  <div class="banner">
    <div class="brand-name"><span>Gentle Paws</span><span>Carolina</span></div>

    <div class="hero-photo" role="img" aria-label="Smiling woman hugging a golden retriever"></div>

    <svg class="blue-band" viewBox="0 0 357 840" aria-hidden="true">
      <path d="M0 409 Q 170 445 357 345 L 357 596 Q 190 622 0 620 Z" fill="var(--band-blue)"/>
    </svg>

    <h1 class="headline">PROFESSIONAL PET CARE<br>FOR WHEN YOU CAN'T<br>BE THERE</h1>
    <p class="tagline">Dog walking &amp;<br>pet sitting.</p>

    <div class="team-photo left" role="img" aria-label="Team member outdoors with a brown dog"></div>
    <div class="team-photo right" role="img" aria-label="Team member holding an orange kitten"></div>

    <div class="section-pill services">OUR SERVICES</div>
    <p class="section-text services">Extended Visits, Pop In Visits, Dog Walking,<br>Pet Taxi, Travel &amp; Adventure Hikes.</p>

    <div class="section-pill offer">WE OFFER</div>
    <p class="section-text offer">Discounts for First Responders,<br>Teachers, &amp; Military</p>

    <div class="footer-bar">www.gentlepawsco.net</div>
  </div>
</div>
</body>
</html>
```